Car Soap Label Design specifically targeting RVs

I am private labeling a car wash soap to specifically target the RV industry. It will be sold in a one gallon jug with a 6"x11" spot to place the label on front and wrap around the two sides. (see attached pics for example of label size) The front of the label I want to have a realistic picture of a high dollar class A RV somehow integrated into the design, and the key features of the soap. I had wordsmithbot design a couple that I kind of like the look of that I will attach, but open to other options. I want something clean and professional looking that will back the premium product I am selling.
The name of my brand is "Blue Harbor Gleam". I want the brand name to be somewhere on the label, but not a main focus. I want the focus to be the product and its benefits. "Premium RV Wash and Wax" as the main verbiage. Benefits... "Developed for Use With Foam Gun or Bucket with Water", "Safe for All RV Exteriors", "Protective Wax Formula", "Enhanced Shine", "Water Repellent", "Streak Free Rinse", "UV Protection". On the side...Directions: 2 Ways of Mixing... Pour Concentrate into Foam Gun Bottle OR Mixing Ratio: 1 Part Wash & Wax / 3 Parts Water in bucket. Apply soap to one side of RV at a time and use carwash brush to easily loosen road film and rinse clean. On the other side... Keep from freezing, Keep Out of Reach of Children. MADE IN USA. Hazardous Ingredients: NONE . NOTICE: The seller and/or manufacturer assumes no responsibility for damage or injury resulting from misuse of this product. No warranties, expressed or implied, are given for the performance or safety of this product.

Target Market(s)

RV industry

Industry/Entity Type

RV/Auto

Requirements
Must have
• Clean, Professional look, size 6" tall and 11" wide
Nice to have
• Realistic Class A RV as part of design

```html
<!DOCTYPE html>
<html lang="en">
<head>
<meta charset="utf-8">
<title>Premium RV Wash &amp; Wax Label</title>
<link href="https://fonts.googleapis.com/css2?family=Poppins:wght@600;700;800;900&display=swap" rel="stylesheet">
<style>
  :root {
    --sky-top: #3f9fdc;
    --sky-mid: #78c0ea;
    --sky-low: #d6eaf6;
    --band-dark: #0b2a5e;
    --band-bright: #1d94e4;
    --stripe: #1570bd;
    --navy: #0d2f63;
    --badge: #1e2f4c;
    --white: #ffffff;
    --dot: #e3955a;
  }
  * { box-sizing: border-box; margin: 0; padding: 0; }
  html, body { width: 1200px; height: 655px; overflow: hidden; background: #fff; }
  body { font-family: "Poppins", sans-serif; }
  .label {
    position: relative; width: 1200px; height: 655px; overflow: hidden;
    background: linear-gradient(180deg, var(--sky-top) 0%, var(--sky-mid) 35%, var(--sky-low) 64%);
  }
  .top-stripe { position: absolute; left: 0; top: 0; width: 1200px; height: 60px; }
  .lower-band {
    position: absolute; left: 0; top: 422px; width: 1200px; height: 233px;
    background: linear-gradient(180deg, var(--band-dark) 0%, #0f4b91 40%, var(--band-bright) 100%);
  }
  .rv-photo {
    position: absolute; left: 240px; top: 118px; width: 675px; height: 332px;
    border-radius: 24px 40px 30px 30px;
    background: linear-gradient(100deg, #c9a48a 0%, #e8d3c0 35%, #3a4658 70%, #8d97a6 100%);
    opacity: .92;
  }
  .pill {
    position: absolute; color: var(--white); font-weight: 800;
    background: linear-gradient(90deg, var(--navy) 0%, #16508f 100%);
    border-radius: 4px 16px 16px 4px; letter-spacing: .3px;
  }
  .directions-title { left: 22px; top: 100px; width: 140px; height: 32px; font-size: 16px; line-height: 32px; padding-left: 10px; }
  .notice-title { left: 922px; top: 158px; width: 100px; height: 30px; font-size: 15px; line-height: 30px; padding-left: 10px; }
  .copy {
    position: absolute; color: var(--white); font-weight: 700;
    font-size: 10.4px; line-height: 12.4px; text-transform: uppercase;
  }
  .directions-copy { left: 22px; top: 140px; width: 210px; }
  .care-copy { left: 922px; top: 101px; width: 270px; }
  .notice-copy { left: 922px; top: 196px; width: 262px; }
  .brand-tab {
    position: absolute; left: 22px; top: 420px; width: 68px; height: 86px;
    background: var(--badge); border-radius: 0 0 18px 18px;
    display: flex; align-items: center; justify-content: center; text-align: center;
  }
  .brand-name { color: var(--white); font-weight: 800; font-size: 10px; line-height: 11px; text-transform: uppercase; }
  .title { position: absolute; color: var(--white); font-weight: 800; line-height: 1; text-transform: uppercase; }
  .title-top { left: 310px; top: 448px; font-size: 57px; letter-spacing: .5px; }
  .title-main { left: 308px; top: 490px; font-size: 87px; letter-spacing: 1px; }
  .benefits { position: absolute; left: 0; top: 575px; width: 1200px; text-align: center; color: var(--white); font-weight: 700; font-size: 13.6px; line-height: 17.5px; text-transform: uppercase; }
  .benefits-row { display: flex; justify-content: center; align-items: center; gap: 6px; }
  .benefits-tag { background: var(--navy); border-radius: 8px; font-size: 8.5px; font-weight: 800; padding: 0 12px; line-height: 15px; margin-right: 4px; }
  .benefit::before { content: ""; display: inline-block; width: 10px; height: 10px; border-radius: 50%; background: var(--dot); margin-right: 6px; vertical-align: 0; }
</style>
</head>
<body>
<main class="label">
  <svg class="top-stripe" viewBox="0 0 1200 60" aria-hidden="true">
    <polygon points="0,0 1200,0 1200,22 0,38" fill="var(--stripe)"/>
    <polygon points="0,38 1200,22 1200,30 0,48" fill="#5fb2e6" opacity=".6"/>
  </svg>

  <div class="lower-band"></div>

  <div class="rv-photo" role="img" aria-label="Realistic luxury class A motorhome with tan and navy swoosh graphics, shown at a three-quarter front angle"></div>

  <div class="pill directions-title">DIRECTIONS:</div>
  <p class="copy directions-copy">
    2 ways of mixing<br>
    pour concentrate into foam gun bottle or mixing ratio: 1 part wash &amp; wax / 3 parts water in bucket.<br>
    apply soap to one side of RV at a time and use carwash brush to easily loosen road film and rinse clean
  </p>

  <p class="copy care-copy">
    Keep from freezing<br>
    Keep out of reach of children.<br>
    Made in USA.<br>
    Hazardous ingredients: none .
  </p>
  <div class="pill notice-title">NOTICE:</div>
  <p class="copy notice-copy">
    The seller and/or manufacturer assumes no responsibility for damage or injury resulting from misuse of this product.<br>
    No warranties, expressed or implied, are given for the performance or safety of this product.
  </p>

  <div class="brand-tab"><span class="brand-name">Blue Harbor Gleam</span></div>

  <h1>
    <span class="title title-top">Premium RV</span>
    <span class="title title-main">Wash &amp; Wax</span>
  </h1>

  <div class="benefits">
    <div class="benefits-row"><span class="benefits-tag">Benefits</span><span class="benefit">Developed for use with foam gun or bucket with water</span></div>
    <div class="benefits-row"><span class="benefit">Safe for all RV exteriors</span><span class="benefit">Protective wax formula</span><span class="benefit">Enhanced shine</span></div>
    <div class="benefits-row"><span class="benefit">Water repellent</span><span class="benefit">Streak free rinse</span><span class="benefit">UV protection</span></div>
  </div>
</main>
</body>
</html>
```